Plakate für Anbieter von Karosserie-Reparaturen und -Services
Zielgruppe
Unser Kunde, die Halden & Brunner AG aus Oberbuchsiten (CH), ist ein Anbieter von Karosserie Reparaturen und Services. Er wird an einem öffentlichen Event teilnehmen und benötigt hierfür ein Plakat um seine Aktivität auf seinem Stand zu bewerben. Diese Aktivität ist für die Besucher die Teilnahme als Fahrer auf der Velocita-Rennbahn auf dem Stand. Hierfür benötigen wir ein Plakat (Format A0, farbig) welches auf das Rennen und die zu gewinneneden Preise aufmerksam macht.
Aufgabenstellung
Das Plakat muss modern, ansprechend, einladend und motivierend sein. Es kann mit Bilder (Vorschläge aus Pixora-Archiv) und Farben gearbeiten werden. Die Farben müssen nicht zwingend einen direkten Bezug zum Logo haben.
Dieser Text muss zwingend ersichtlich sein:
→ 15 Runden sind zu fahren
→ die schnellste Zeit gewinnt
Zu gewinnen gibt es
1. Preis: Gutschein im Wert von CHF 1'000.- von Rovanta
2. Preis: Fahrzeugreinigung inkl. Politur im Wert von CHF 800.-
3. Preis Werkstatt-Gutschein im Wert von CHF 400.-
Nebst dem Text benötigt es noch einen 'Call to Action' > z.B. Jetzt mitmachen und gewinne oder so ähnlich. Zudem benötigst es noch einen Platzhalter für ein zweites Logo. Dieses ist aktuell noch nicht definiert und wird dann erst bei der Finalisierung eingefügt.

```html
<!DOCTYPE html>
<html lang="de">
<head>
<meta charset="utf-8">
<title>Halden &amp; Brunner – Rennen</title>
<link rel="stylesheet" href="https://fonts.googleapis.com/css2?family=Roboto:wght@400;500;700&family=Oswald:wght@500&display=swap">
<style>
  :root {
    --page-bg: #cfe5ef;
    --paper: #ffffff;
    --brand-blue: #1c63a3;
    --cyan: #0aa9e8;
    --yellow: #fbbd40;
    --ink: #2b2b2b;
    --dark-band: #333333;
    --white: #ffffff;
  }
  html, body {
    margin: 0; padding: 0;
    width: 982px; height: 1200px;
    overflow: hidden;
    background: var(--page-bg);
  }
  .poster {
    position: absolute;
    left: 153px; top: 150px;
    width: 675px; height: 900px;
    display: block;
  }
  .sans { font-family: "Roboto", Arial, sans-serif; }
  .condensed { font-family: "Oswald", "Arial Narrow", sans-serif; font-weight: 500; }
  .headline { fill: var(--brand-blue); font-weight: 700; font-size: 31px; }
  .subhead { fill: var(--ink); font-weight: 400; font-size: 29px; }
  .prize-text { font-size: 15px; }
  .contact { fill: var(--white); font-size: 14px; letter-spacing: .4px; }
  .cta { fill: var(--yellow); font-weight: 700; font-size: 17px; }
</style>
</head>
<body>
<svg class="poster" viewBox="0 0 590 787" xmlns="http://www.w3.org/2000/svg">
  <defs>
    <clipPath id="paper-clip"><rect width="590" height="787"/></clipPath>
    <linearGradient id="welder-tones" x1="0" y1="0" x2="1" y2="1">
      <stop offset="0" stop-color="#8a96a6"/>
      <stop offset=".5" stop-color="#2f58a8"/>
      <stop offset="1" stop-color="#e8b070"/>
    </linearGradient>
    <linearGradient id="garage-tones" x1="0" y1="0" x2="1" y2="1">
      <stop offset="0" stop-color="#d4d6da"/>
      <stop offset=".55" stop-color="#3a3d44"/>
      <stop offset="1" stop-color="#d6372b"/>
    </linearGradient>
    <filter id="soft-shadow" x="-20%" y="-20%" width="140%" height="140%">
      <feDropShadow dx="0" dy="3" stdDeviation="5" flood-color="#000" flood-opacity=".3"/>
    </filter>
  </defs>

  <rect class="paper" width="590" height="787" fill="var(--paper)"/>

  <g class="hero" clip-path="url(#paper-clip)">
    <circle class="photo-welder" cx="135" cy="165" r="130" fill="url(#welder-tones)"
            role="img" aria-label="Foto: Mechaniker in blauer Arbeitskleidung beim Schweissen mit Funkenflug"/>
    <circle class="photo-garage" cx="400" cy="140" r="174" fill="var(--paper)"/>
    <circle cx="400" cy="140" r="170" fill="url(#garage-tones)"
            role="img" aria-label="Foto: Werkstatt mit rotem Sportwagen auf der Hebebühne und Mechaniker"/>
    <circle class="logo-disc" cx="298" cy="5" r="148" fill="var(--paper)"/>
    <circle cx="298" cy="5" r="140" fill="var(--brand-blue)"/>
    <g class="logo-name sans">
      <circle cx="208" cy="52" r="11" fill="var(--white)"/>
      <text x="228" y="46" fill="var(--white)" font-size="12" font-weight="700" letter-spacing=".5">CARROSSERIE</text>
      <text x="228" y="66" fill="var(--white)" font-size="17" font-weight="700">HALDEN+BRUNNER</text>
    </g>
  </g>

  <g class="rules sans">
    <g class="arrow" stroke="var(--ink)" stroke-width="4" fill="none" stroke-linecap="round" stroke-linejoin="round">
      <path d="M33 338 H60 M49 327 L60 338 L49 349"/>
      <path d="M33 384 H60 M49 373 L60 384 L49 395"/>
    </g>
    <text class="headline" x="73" y="349">15 RUNDEN SIND ZU FAHREN</text>
    <text class="headline" x="73" y="395">DIE SCHNELLSTE ZEIT GEWINNT</text>
    <text class="subhead" x="295" y="442" text-anchor="middle">ZU GEWINNEN GIBT ES</text>
  </g>

  <path class="contact-band" d="M0 787 Q295 520 590 787 Z" fill="var(--dark-band)"/>

  <g class="prizes sans" text-anchor="middle">
    <g class="prize prize-first">
      <circle cx="106" cy="565" r="104" fill="var(--paper)" filter="url(#soft-shadow)"/>
      <circle cx="106" cy="565" r="95" fill="var(--brand-blue)"/>
      <circle cx="106" cy="488" r="26" fill="var(--paper)"/>
      <circle cx="106" cy="488" r="21" fill="var(--yellow)"/>
      <text x="106" y="485" fill="var(--white)" font-size="11">1.</text>
      <text x="106" y="498" fill="var(--white)" font-size="11">PREIS:</text>
      <text x="106" y="543" fill="var(--white)" font-size="21">GUTSCHEIN IM</text>
      <text x="106" y="567" fill="var(--white)" font-size="21">WERT VON</text>
      <text class="condensed" x="106" y="603" fill="var(--yellow)" font-size="31">CHF 1'000.-</text>
      <text x="106" y="627" fill="var(--white)" font-size="14">- VON ROVANTA</text>
    </g>
    <g class="prize prize-second">
      <circle cx="295" cy="565" r="104" fill="var(--paper)" filter="url(#soft-shadow)"/>
      <circle cx="295" cy="565" r="95" fill="var(--cyan)"/>
      <circle cx="295" cy="488" r="26" fill="var(--paper)"/>
      <circle cx="295" cy="488" r="21" fill="var(--brand-blue)"/>
      <text x="295" y="485" fill="var(--white)" font-size="11">2.</text>
      <text x="295" y="498" fill="var(--white)" font-size="11">PREIS:</text>
      <text x="295" y="537" fill="var(--white)" font-size="15">FAHRZEUGREINIGUNG</text>
      <text x="295" y="557" fill="var(--white)" font-size="15">INKL. POLITUR</text>
      <text x="295" y="576" fill="var(--white)" font-size="15">IM WERT VON</text>
      <text class="condensed" x="295" y="614" fill="#111" font-size="34">CHF 800.-</text>
    </g>
    <g class="prize prize-third">
      <circle cx="484" cy="565" r="104" fill="var(--paper)" filter="url(#soft-shadow)"/>
      <circle cx="484" cy="565" r="95" fill="var(--yellow)"/>
      <circle cx="484" cy="488" r="26" fill="var(--paper)"/>
      <circle cx="484" cy="488" r="21" fill="var(--cyan)"/>
      <text x="484" y="485" fill="var(--white)" font-size="11">3.</text>
      <text x="484" y="498" fill="var(--white)" font-size="11">PREIS:</text>
      <text x="484" y="549" fill="var(--ink)" font-size="14.5">WERKSTATT-GUTSCHEIN</text>
      <text x="484" y="568" fill="var(--ink)" font-size="14.5">IM WERT VON</text>
      <text class="condensed" x="484" y="609" fill="#111" font-size="34">CHF 400.-</text>
    </g>
  </g>

  <g class="call-to-action sans">
    <text class="cta" x="154" y="702">JETZT MITMACHEN UND GEWINNE</text>
    <g class="icons" fill="none" stroke="var(--yellow)" stroke-width="1.4">
      <path d="M157 719 q1 -2 3 -1 l2 3 q0 2 -2 2 q1 3 4 4 q0 -2 2 -2 l3 2 q1 2 -1 3 q-8 1 -11 -11 z" fill="var(--yellow)" stroke="none"/>
      <rect x="156" y="740" width="13" height="9"/>
      <path d="M156 740 L162.5 745 L169 740"/>
      <circle cx="162.5" cy="764" r="6.5"/>
      <path d="M156 764 H169 M162.5 757.5 q-4 6.5 0 13 M162.5 757.5 q4 6.5 0 13"/>
    </g>
    <text class="contact" x="178" y="728">+41 32 555 01 77</text>
    <text class="contact" x="178" y="748">info@halden-brunner.ch</text>
    <text class="contact" x="178" y="769">halden-brunner.ch</text>
  </g>
</svg>
</body>
</html>
```